Looking for an Innovative Print Design (Service Directory)

We need a new design for our advertisement within a printed colour services directory.

We are a compensation law firm called Velbrook Compensation Lawyers. Feel free to take a browse of our website www.velbrooklegal.com.au to get an idea of what we do and the kind of firm we are.

We are in the process of redeveloping our website and as such, so please don't adhere to the design principles of the current site- impress us with your originality!

On top of any editable formats, your final submissions must include a .pdf copy.
The same design will need to be presented in two dimensions:

- 154mm x 118mm (B1/B2 Half Page);
- 175mm x 113mm (B4 Half Page).

[For more information refer to attached Pdf.]

We have attached for you a few examples of other firms' designs (Sample1,2,3). These are by no means good, or what we're after, it's just to provide you with an idea of what sort of advertisements go into the service directory.

Hi all,

We want to emphasise that a priority of the design is that it must look:
• Professional
• Sophisticated
Please do not hesitate to use completely different colour schemes to the ones that are on our website- as we have said, our website will change in the near future, so cohesion between the current project and the website is not necessary!

Thanks!

Thank you for your submissions so far. There are some great ideas hidden in there. 

An issue we are having is that most of you are conforming to the same understanding of what it should look like. Remember that there is NO NEED to be bound by the image of firm as is. That is, feel free to use a different colour logo.

For inspiration, we relate well to the design aesthetics of: http://www.tinfernstudio.co.uk/

Look forward to seeing your 'out of the box' submissions. 

Reason: We've received a large amount of fantastic designs. However, what we're really looking for is something original. Please feel free to think outside the box (the final design doesn't need to look like a print ad), and construct a design that is completely incongruous with our website! While we do appreciate a minimalistic design, we have yet to receive something that really grabs your attention with its visuals. We're not sure but this may or may not be achieved with a full colour design. Thanks for all your submissions- they all have some features that really click with us. We look forward to the next wave of submissions!

Target Market(s)

We have various target markets, including mainly families, elderly people, blue collar workers.

These are individuals who are looking for assistance. They feel helpless or wronged.

Keep in mind that the people accessing these are those who prefer going to a printed directory rather than using a google search.

Industry/Entity Type

Law Firm

Font styles to use
Serif
Sans Serif

Requirements
Must have
• - Our name 'Velbrook Compensation Lawyers'
- Our logo (attached as logo.eps, logo.png, and logo.tif)
- Must include phone number as 1300 XXX XXX (this must be prominent)
- Must include the following service areas in these words: Motor vehicle claims, medical claims, superannuation claims, Workplace claims, negligence claims
- Our email address: info@velbrooklegal.com.au
- Our website address: www.velbrooklegal.com.au
- The following catchphrases: '98% success rate', and 'No win no fee' in those words
- Our location '412 Carvel Lane, Smithville, SYDNEY'
- For sizing dimensions, we need one in 154mm x 118mm and also a design in 175mm x 113mm (B4 Half Page) [refer to pdf attached]
Nice to have
• - Text indicating free initial consulatation
- Professional colour scheme
- As our website will be changed, do not worry about making the advertisement cohesive with our website design
- We want the design to be modern, but still professional
- Clean typeface
- No gradient colour scheme
- When designing, if you are looking to place more text onto the advertisement, these may be some considerations (feel free to change the wording): Accredited specialists, home and hospital visits

```html
<!DOCTYPE html>
<html lang="en">
<head>
<meta charset="utf-8">
<title>Velbrook Compensation Lawyers – Directory Advertisements</title>
<link rel="stylesheet" href="https://fonts.googleapis.com/css2?family=Arimo:ital,wght@0,400;0,700;1,400&display=swap">
<style>
  :root{
    --backdrop:#0b0b0b;
    --orange:#f36f21;
    --charcoal:#3d423f;
    --ink:#3a3d3c;
    --name-grey:#4a4d4c;
    --rule:#6b6e6d;
    --white:#ffffff;
    --photo-light:#f4f4f3;
    --photo-dark:#b9bbbd;
  }
  *{box-sizing:border-box;margin:0;padding:0}
  html,body{width:1200px;height:1200px;overflow:hidden;background:var(--backdrop)}
  body{position:relative;font-family:"Arimo",Arial,sans-serif}

  .size-label{position:absolute;color:var(--white);font-style:italic;font-size:20px;line-height:31px;text-align:center;letter-spacing:.5px}
  .size-label--half{left:200px;top:54px;width:320px}
  .size-label--b4{left:734px;top:1078px;width:320px}

  .ad{position:absolute;background:var(--orange)}
  .ad__panel{position:absolute;background:var(--white);overflow:hidden}
  .ad__photo{position:absolute;background:linear-gradient(160deg,var(--photo-light) 0%,#dedfe0 45%,var(--photo-dark) 100%)}
  .ad__band{position:absolute;left:0;top:0}
  .ad__footer{position:absolute;left:0;width:100%;text-align:center;color:var(--white);font-weight:700;line-height:28px;white-space:nowrap}

  .brand__dot{position:absolute;border-radius:50%;background:var(--orange)}
  .brand__name{position:absolute;color:var(--name-grey);font-weight:400;line-height:1;white-space:nowrap}
  .brand__rule{position:absolute;height:2px;background:var(--rule)}

  .services{position:absolute;list-style:none;color:var(--ink);font-weight:700;white-space:nowrap}
  .services li{display:flex;align-items:center}
  .services li::before{content:"";flex:none;border-radius:50%;border:solid var(--orange)}

  .promise{position:absolute;color:var(--white);font-weight:700;text-align:center;white-space:nowrap}
  .call{position:absolute;color:var(--white);font-weight:700;white-space:nowrap;line-height:1.2}
  .contacts{position:absolute;list-style:none;color:var(--white);font-weight:700;white-space:nowrap}
  .contacts li{display:flex;align-items:center}
  .contacts svg{flex:none;fill:var(--orange)}

  /* 154 x 118 */
  .ad--half{left:538px;top:32px;width:620px;height:636px}
  .ad--half .ad__panel{left:16px;top:16px;width:588px;height:576px}
  .ad--half .ad__photo{left:0;top:162px;width:226px;height:290px}
  .ad--half .brand__dot{left:10px;top:14px;width:130px;height:130px}
  .ad--half .brand__name--main{left:170px;top:28px;font-size:70px;letter-spacing:.5px}
  .ad--half .brand__name--sub{left:172px;top:96px;font-size:23px;letter-spacing:3.2px;font-weight:700}
  .ad--half .brand__rule{left:142px;top:156px;width:438px}
  .ad--half .services{left:238px;top:182px;font-size:25px}
  .ad--half .services li{height:39px;gap:11px}
  .ad--half .services li::before{width:18px;height:18px;border-width:5px}
  .ad--half .promise{left:0;top:481px;width:236px;font-size:23px;line-height:35px}
  .ad--half .call{left:240px;top:460px;font-size:32px}
  .ad--half .contacts{left:243px;top:502px;font-size:16px}
  .ad--half .contacts li{height:21px;gap:6px}
  .ad--half .ad__footer{top:600px;font-size:20px;letter-spacing:.8px}

  /* 175 x 113 */
  .ad--b4{left:42px;top:712px;width:692px;height:447px}
  .ad--b4 .ad__panel{left:13px;top:14px;width:665px;height:394px}
  .ad--b4 .ad__photo{left:0;top:0;width:305px;height:300px}
  .ad--b4 .brand__dot{left:311px;top:18px;width:80px;height:80px}
  .ad--b4 .brand__name--main{left:405px;top:26px;font-size:43px;letter-spacing:.5px}
  .ad--b4 .brand__name--sub{left:407px;top:72px;font-size:14px;letter-spacing:2px;font-weight:700}
  .ad--b4 .brand__rule{left:311px;top:114px;width:344px}
  .ad--b4 .services{left:317px;top:122px;font-size:20px;letter-spacing:.5px}
  .ad--b4 .services li{height:27.6px;gap:7px}
  .ad--b4 .services li::before{width:13px;height:13px;border-width:3.5px}
  .ad--b4 .promise{left:0;top:316px;width:310px;font-size:23px;line-height:27px;letter-spacing:1.5px}
  .ad--b4 .call{left:317px;top:300px;font-size:26px;letter-spacing:.5px}
  .ad--b4 .contacts{left:318px;top:327px;font-size:14.5px}
  .ad--b4 .contacts li{height:20.5px;gap:6px}
  .ad--b4 .ad__footer{top:410px;font-size:20px;letter-spacing:.8px}
</style>
</head>
<body>

<p class="size-label size-label--half">154mm x 118mm<br>(B1/B2 Half Page)</p>

<section class="ad ad--half" aria-label="Velbrook advertisement, 154mm by 118mm">
  <div class="ad__panel">
    <span class="brand__dot"></span>
    <span class="brand__name brand__name--main">VELBROOK</span>
    <span class="brand__name brand__name--sub">COMPENSATION LAWYERS</span>
    <span class="brand__rule"></span>
    <div class="ad__photo" role="img" aria-label="Photograph of three business people in suits shaking hands, seen from above"></div>
    <ul class="services">
      <li>Motor vehicle claims</li>
      <li>Medical claims</li>
      <li>Superannuation claims</li>
      <li>Workplace claims</li>
      <li>Negligence claims</li>
    </ul>
    <svg class="ad__band" width="588" height="576" viewBox="0 0 588 576" aria-hidden="true">
      <path d="M0,390 C150,432 320,446 588,372 L588,576 L0,576 Z" fill="var(--orange)"/>
      <path d="M0,412 C150,448 330,456 588,394 L588,576 L0,576 Z" fill="var(--charcoal)"/>
    </svg>
    <p class="promise">No win no fee<br>98% success rate</p>
    <p class="call">Call 1300 XXX XXX</p>
    <ul class="contacts">
      <li><svg width="11" height="11" viewBox="0 0 10 10"><circle cx="5" cy="5" r="4.5"/></svg>www.velbrooklegal.com.au</li>
      <li><svg width="11" height="9" viewBox="0 0 11 8"><rect width="11" height="8" rx="1"/></svg>info@velbrooklegal.com.au</li>
      <li><svg width="11" height="14" viewBox="0 0 10 14"><path d="M5 0a5 5 0 0 1 5 5c0 3.5-5 9-5 9S0 8.5 0 5a5 5 0 0 1 5-5zm0 3a2 2 0 1 0 0 4 2 2 0 0 0 0-4z"/></svg>412 Carvel Lane, Smithville, Sydney</li>
    </ul>
  </div>
  <p class="ad__footer">Accredited specialists, home and hospital visits.</p>
</section>

<section class="ad ad--b4" aria-label="Velbrook advertisement, 175mm by 113mm">
  <div class="ad__panel">
    <div class="ad__photo" role="img" aria-label="Photograph of three business people in suits shaking hands, seen from above"></div>
    <span class="brand__dot"></span>
    <span class="brand__name brand__name--main">VELBROOK</span>
    <span class="brand__name brand__name--sub">COMPENSATION LAWYERS</span>
    <span class="brand__rule"></span>
    <ul class="services">
      <li>Motor vehicle claims</li>
      <li>Medical claims</li>
      <li>Superannuation claims</li>
      <li>Workplace claims</li>
      <li>Negligence claims</li>
    </ul>
    <svg class="ad__band" width="665" height="394" viewBox="0 0 665 394" aria-hidden="true">
      <path d="M0,252 C180,292 390,300 665,246 L665,394 L0,394 Z" fill="var(--orange)"/>
      <path d="M0,269 C180,304 400,310 665,263 L665,394 L0,394 Z" fill="var(--charcoal)"/>
    </svg>
    <p class="promise">No win no fee<br>98% success rate</p>
    <p class="call">Call 1300 XXX XXX</p>
    <ul class="contacts">
      <li><svg width="10" height="10" viewBox="0 0 10 10"><circle cx="5" cy="5" r="4.5"/></svg>www.velbrooklegal.com.au</li>
      <li><svg width="10" height="8" viewBox="0 0 11 8"><rect width="11" height="8" rx="1"/></svg>info@velbrooklegal.com.au</li>
      <li><svg width="10" height="13" viewBox="0 0 10 14"><path d="M5 0a5 5 0 0 1 5 5c0 3.5-5 9-5 9S0 8.5 0 5a5 5 0 0 1 5-5zm0 3a2 2 0 1 0 0 4 2 2 0 0 0 0-4z"/></svg>412 Carvel Lane, Smithville, Sydney</li>
    </ul>
  </div>
  <p class="ad__footer">Accredited specialists, home and hospital visits.</p>
</section>

<p class="size-label size-label--b4">175mm x 113mm<br>(B4 Half Page)</p>

</body>
</html>
```